Bravel Acres Business Cards

design business cards for our new business should match my Corvane Quotations business cards

Contact Information for Business Card

2817 W 68th N St
Tulsa, OK 74592

Requirements
Must have
• should match logo colors

```html
<!DOCTYPE html>
<html lang="en">
<head>
<meta charset="utf-8">
<title>Bravel Acres Business Cards</title>
<link href="https://fonts.googleapis.com/css2?family=Open+Sans:wght@400;700&family=Poppins:wght@300;400;500;600&display=swap" rel="stylesheet">
<style>
  :root {
    --bg: #1d1d1f;
    --navy: #232f6e;
    --red: #c8203a;
    --paper: #ffffff;
    --pattern-light: #f3f3f3;
    --pattern-mid: #e4e4e4;
    --deep-teal: #0d2c33;
    --leaf-green: #7cc242;
    --sea-green: #3dbb9c;
    --ink-light: #f2f4f4;
    --rule: #5f7b80;
  }
  html, body {
    margin: 0;
    width: 1200px;
    height: 880px;
    overflow: hidden;
    background: var(--bg);
  }
  .canvas {
    position: relative;
    width: 1200px;
    height: 880px;
  }
  .card {
    position: absolute;
    width: 560px;
    height: 320px;
    border-radius: 16px;
    overflow: hidden;
    box-shadow: 0 18px 40px rgba(0,0,0,.55);
  }

  /* Corvane Quotations front */
  .card--quotations {
    left: 60px;
    top: 90px;
    background: var(--paper);
    border-top: 16px solid var(--navy);
    border-bottom: 16px solid var(--navy);
    box-sizing: border-box;
  }
  .pattern-area {
    position: absolute;
    inset: 18px 24px;
    border-radius: 6px;
    background: linear-gradient(160deg, var(--pattern-light), var(--pattern-mid));
  }
  .quotations-name {
    position: absolute;
    left: 50%;
    top: 50%;
    transform: translate(-50%, -50%);
    font-family: "Open Sans", sans-serif;
    font-weight: 700;
    font-size: 34px;
    line-height: 1;
    color: var(--navy);
    background: var(--paper);
    padding: 14px 22px;
    border-radius: 6px;
    white-space: nowrap;
    display: flex;
    align-items: center;
    gap: 12px;
  }
  .quotations-name .mark {
    width: 18px;
    height: 18px;
    background: var(--red);
  }

  /* Bravel Acres card */
  .card--acres {
    left: 580px;
    top: 470px;
    background: var(--deep-teal);
    font-family: "Poppins", sans-serif;
    color: var(--ink-light);
  }
  .acres-name {
    position: absolute;
    left: 36px;
    top: 118px;
    width: 230px;
    font-weight: 600;
    font-size: 40px;
    line-height: 44px;
    color: var(--leaf-green);
    display: flex;
    align-items: center;
    gap: 10px;
  }
  .acres-name .mark {
    flex: none;
    width: 14px;
    height: 14px;
    border-radius: 50%;
    background: var(--leaf-green);
  }
  .divider {
    position: absolute;
    left: 282px;
    top: 40px;
    width: 1px;
    height: 170px;
    background: var(--rule);
  }
  .person {
    position: absolute;
    left: 306px;
    top: 44px;
  }
  .person__name {
    margin: 0;
    font-weight: 500;
    font-size: 25px;
    letter-spacing: 1px;
    color: var(--sea-green);
  }
  .person__role {
    margin: 0;
    font-size: 13px;
    font-weight: 400;
  }
  .contact-list {
    list-style: none;
    margin: 0;
    padding: 0;
    position: absolute;
    left: 306px;
    top: 118px;
    font-size: 13px;
    line-height: 22px;
  }
  .contact-list li {
    display: flex;
    align-items: center;
    gap: 9px;
  }
  .contact-list svg { width: 15px; height: 15px; flex: none; }
  .address {
    position: absolute;
    left: 0;
    right: 0;
    bottom: 34px;
    margin: 0;
    text-align: center;
    font-size: 13px;
    letter-spacing: 2px;
    text-transform: uppercase;
  }
</style>
</head>
<body>
<main class="canvas">

  <section class="card card--quotations" aria-label="Corvane Quotations business card">
    <div class="pattern-area" role="img" aria-label="Light grey background pattern of service words"></div>
    <div class="quotations-name"><span class="mark"></span>Corvane Quotations</div>
  </section>

  <section class="card card--acres" aria-label="Bravel Acres business card">
    <div class="acres-name"><span class="mark"></span>Bravel Acres</div>
    <div class="divider"></div>
    <div class="person">
      <p class="person__name">DALEN MERCER</p>
      <p class="person__role">Managing Director</p>
    </div>
    <ul class="contact-list">
      <li>
        <svg viewBox="0 0 16 16"><circle cx="8" cy="8" r="7.5" fill="#3dbb9c"/><path d="M5.3 4.5l1.4 1.6-.7 1c.5 1 1.3 1.8 2.3 2.3l1-.7 1.6 1.4-.8 1.2c-2.8-.3-5.3-2.8-5.6-5.6z" fill="#0d2c33"/></svg>
        +1 918 555 0142
      </li>
      <li>
        <svg viewBox="0 0 16 16"><circle cx="8" cy="8" r="7.5" fill="#3dbb9c"/><rect x="5.5" y="4" width="5" height="8" rx="1" fill="none" stroke="#0d2c33" stroke-width="1.2"/></svg>
        +1 918 555 0178
      </li>
      <li>
        <svg viewBox="0 0 16 16"><circle cx="8" cy="8" r="7.5" fill="#3dbb9c"/><rect x="4" y="5" width="8" height="6" fill="none" stroke="#0d2c33" stroke-width="1.2"/><path d="M4 5l4 3.5L12 5" fill="none" stroke="#0d2c33" stroke-width="1.2"/></svg>
        hello@bravelacres.com
      </li>
      <li>
        <svg viewBox="0 0 16 16"><circle cx="8" cy="8" r="7.5" fill="#3dbb9c"/><circle cx="8" cy="8" r="4" fill="none" stroke="#0d2c33" stroke-width="1.1"/><path d="M4 8h8M8 4c-2 2.5-2 5.5 0 8M8 4c2 2.5 2 5.5 0 8" fill="none" stroke="#0d2c33" stroke-width="1"/></svg>
        www.bravelacres.com
      </li>
    </ul>
    <p class="address">2817 W 68th N St , Tulsa, OK 74592</p>
  </section>

</main>
</body>
</html>
```